Nutrigenomics Business card design

Nutrigenomics is an exciting emerging field where I sequence the DNA from a saliva swab and then tailor a personalised nutritional program according to the persons genetics. It is possible to turn down undesirable genes that may be stuck "on" all the time causing inflammation etc. Equally important we switch "on" genes that might be stuck "off" as is often the case with autism. A large portion of my clients are autistic children. We see huge changes in functionality with the appropriate changes in diet to regulate their gene expression. This technology is definitely the way of the future.
I need a logo that will clearly show the combination of genetics with nutrition. The word "Nutrigenomics" still isn't in common use yet. I'm thinking maybe a DNA helix - (I think most people associate a helix with DNA or genes, but I'm open to suggestions) Combined somehow with food - preferably vegetables/ fruit/ meat/eggs etc. Definitely not grains or dairy - we take autistic kids off those 2 food groups straight away.
Green in it somewhere? I somehow associates healthy living / whole foods nutrition with the colour green. You guys know more about colours than me :-)
Maybe a helix could morph into a body shape filled with foods (along the lines of "you are what you eat" or something...)

Target Market(s)

The majority of my clients to date are people in their 40's wanting to improve their health or their children's health.

Industry/Entity Type

Nutrition

Contact Information for Business Card

Front of card:
Dr Moira Crandle (B App Sci, PhD Molecular Pathology)
Certified Vitalorin Practitioner and LUMO Nutritionist
247 Pellbrook Rd, Pellbrook
0417836254
dr.moiracrandle@examplemail.com.au
drmoiracrandle.com.au
Back of card:
Small Photo of me, Dr Moira Crandle
Specialises in Autism, ADHD, Fussy Eaters, Gut Issues, Food Intolerances, Healthy Ageing

Logo Text

Dr Moira Crandle

Logo styles of interest
Pictorial/Combination Logo
Character Logo
Requirements
Must have
• A logo showing a clear link between genes and nutrition
The box for what I want written on the card is not coming up when I try to edit so I'll put it here....
Front of card:
Dr Moira Crandle
(B App Sci, PhD Molecular Pathology) in smaller writing under my name

Certified Nutrigenomist
Certified LUMO Nutritionist

then use your nice symbols for the address, ph etc as below

247 Pellbrook Rd, Pellbrook
0417836254
dr.moiracrandle@examplemail.com.au
www.drmoiracrandle.com.au

Back of card:
Small Photo of me
Dr Moira Crandle
Specialises in:
Nutrigenomics
Healthy Ageing
Autism / ADHD
Gut Issues
Food Intolerances
Should not have
• No bread or grains of any sort
No dairy - milk cheese etc

```html
<!DOCTYPE html>
<html lang="en">
<head>
<meta charset="utf-8">
<title>Dr Moira Crandle – Business Card</title>
<link href="https://fonts.googleapis.com/css2?family=Source+Sans+3:wght@300;400;600&display=swap" rel="stylesheet">
<style>
  :root {
    --backdrop: #8a8a8a;
    --brand-blue: #137dc1;
    --panel-grey: #c9c9c9;
    --rule-white: #eeeeee;
    --card-white: #ffffff;
    --card-fade: #e2e2e2;
    --ink: #1e1e1e;
    --corner-grey: #666666;
  }
  * { margin: 0; padding: 0; box-sizing: border-box; }
  html, body { width: 1200px; height: 750px; overflow: hidden; }
  body {
    background: var(--backdrop);
    font-family: "Source Sans 3", "Myriad Pro", sans-serif;
    position: relative;
  }
  .card {
    position: absolute;
    top: 215px;
    width: 560px;
    height: 320px;
    overflow: hidden;
    box-shadow: 0 6px 18px rgba(0,0,0,.25);
  }

  /* Back of card */
  .card-back { left: 25px; background: var(--card-white); }
  .portrait {
    position: absolute; left: 0; top: 0; width: 195px; height: 100%;
    background: linear-gradient(160deg, #9cb47a 0%, #d9a25c 30%, #7a3f20 60%, #2a1710 100%);
  }
  .name-band {
    position: absolute; left: 195px; top: 22px; right: 0; height: 50px;
    background: var(--brand-blue); color: var(--card-white);
    font-weight: 300; font-size: 30px; line-height: 50px; padding-left: 18px;
  }
  .specialties-label {
    position: absolute; left: 213px; top: 82px;
    color: var(--brand-blue); font-size: 17px; font-weight: 400;
  }
  .specialties {
    position: absolute; left: 258px; top: 108px; width: 245px; bottom: 0;
    background: var(--panel-grey); list-style: none;
  }
  .specialties li {
    height: 35px; line-height: 35px; padding-left: 16px;
    font-size: 17px; font-weight: 300; color: var(--ink);
    border-bottom: 1px solid var(--rule-white);
  }

  /* Front of card */
  .card-front {
    left: 615px;
    background: linear-gradient(180deg, var(--card-fade) 0%, var(--card-white) 75%);
  }
  .identity { position: absolute; left: 24px; top: 118px; width: 272px; }
  .identity-name { color: var(--brand-blue); font-size: 14px; font-weight: 600; line-height: 1.3; }
  .identity-role { color: var(--ink); font-size: 10.5px; font-weight: 400; margin-top: 3px; }
  .divider {
    position: absolute; left: 306px; top: 82px; width: 1.5px; height: 100px;
    background: var(--brand-blue);
  }
  .contacts { position: absolute; left: 322px; top: 90px; list-style: none; }
  .contacts li {
    display: flex; align-items: center; gap: 8px;
    font-size: 12px; color: var(--ink); height: 22px;
  }
  .contacts svg { width: 12px; height: 12px; flex: none; }
  .edge-band { position: absolute; left: 0; bottom: 0; width: 100%; height: 80px; }
</style>
</head>
<body>

<section class="card card-back">
  <div class="portrait" role="img" aria-label="Portrait photo of Dr Moira Crandle"></div>
  <h1 class="name-band">Dr Moira Crandle</h1>
  <p class="specialties-label">Specialises in</p>
  <ul class="specialties">
    <li>Autism</li>
    <li>ADHD</li>
    <li>Fussy Eaters</li>
    <li>Gut Issues</li>
    <li>Food Intolerances</li>
    <li>Healthy Ageing</li>
  </ul>
</section>

<section class="card card-front">
  <div class="identity">
    <p class="identity-name">Dr Moira Crandle (B App Sci, PhD Molecular Pathology)</p>
    <p class="identity-role">Certified Vitalorin Practitioner and LUMO Nutritionist</p>
  </div>
  <div class="divider"></div>
  <ul class="contacts">
    <li>
      <svg viewBox="0 0 12 12"><path d="M6 0.5a4 4 0 0 1 4 4c0 3-4 7-4 7s-4-4-4-7a4 4 0 0 1 4-4z" fill="var(--brand-blue)"/></svg>
      247 Pellbrook Rd, Pellbrook 0417836254
    </li>
    <li>
      <svg viewBox="0 0 12 12"><rect x="0.5" y="2.5" width="11" height="7.5" fill="var(--brand-blue)"/><path d="M0.5 2.5l5.5 4 5.5-4" stroke="#fff" fill="none"/></svg>
      dr.moiracrandle@examplemail.com.au
    </li>
    <li>
      <svg viewBox="0 0 12 12"><g fill="none" stroke="var(--brand-blue)" stroke-width="1"><circle cx="6" cy="6" r="5"/><ellipse cx="6" cy="6" rx="2.2" ry="5"/><path d="M1 6h10"/></g></svg>
      drmoiracrandle.com.au
    </li>
  </ul>
  <svg class="edge-band" viewBox="0 0 560 80" preserveAspectRatio="none">
    <path d="M505 0 H560 V58 H470 C488 50 492 10 505 0 Z" fill="var(--corner-grey)"/>
    <path d="M0 80 V66 L478 66 C490 60 494 36 500 20 L560 18 V80 Z" fill="var(--brand-blue)"/>
  </svg>
</section>

</body>
</html>
```